Migration and redesign of existing website to WordPress using DIVI 3

I. TASK OBJECTIVE:
- Redesign our existing website www.calderwynhealth.com.au with a fresh new look and migrate to new Wordpress site based on DIVI3 theme. The site will contain the same basic functionality as the existing site (with some small changes).

II. STYLE/ DESIGN ASPECT:
As an example of a site that I like the look of, see https://tanglorix.com/. I like the use of shadows, and this would go well with the little animations you can do with Divi (e.g. when hovering over pics).

1. What I am looking for is a design which has lots of white space, is modern and friendly looking (but still not too cute or frivolous, as we are a medical practice)
2. DESIGN that is NOT TOO rectangular or blocky.
3. Please take into consideration our Users are Older market, so any icons or navigation features need to be very easy to understand and not too small.
4. Must be easy to navigate
5. We are are happy to go with a new colour scheme, and are working on some ideas for this, but happy to take suggestions.

III. SPECIFICATIONS:
1. 5+ Pages (should flow like the current site)
2. Using Wordpress Divi 3 theme.
3. I'd like every page to have a "book now" button and a contact form in a sidebar so that users can click the button or fill in the contact form without scrolling at all. EXCEPT ON THE HOME PAGE, where there should still be a book now button (maybe on the top right in the header of all pages?), and maybe a contact us button which scrolls down to the contact area at the bottom of the HOME page. I don't think a side bar is necessarily required on the home page, but if you think it makes sense from a design perspective please let me know.
4. AT THE BOTTOM OF THE PAGE, just above the FOOTER, I'd like a row of trust logos for various organisations that we are affiliated with. (A list of this company will be provided later but you could temporarily use placeholders)

Once we have a structure in place, we can migrate most of the content. Please let me know if I'm not being clear or you need further information.

Target Market(s)

Podiatry Customers and Referrors

Industry/Entity Type

Health Care

Coding

Coded - Design and coding required

Number of Pages Required

5+ page

Colors

Designer to choose colors to be used in the design.

Requirements
Must have
• Simple to navigate.
• Contact/booking details on most if not all pages - please see specification above
• Section for Trusted Affiliates above the footer
• Wordpress using Divi3 Theme
Nice to have
• Not too busy with the design. Plenty of white space or light background.
Should not have
• Should not be complicated to navigate.
• TOO rectangular or blocky designs

```html
<!DOCTYPE html>
<html lang="en">
<head>
<meta charset="utf-8">
<title>Calderwyn Foot &amp; Ankle Clinic</title>
<link href="https://fonts.googleapis.com/css2?family=Oswald:wght@400;500&family=Lato:wght@400;700&display=swap" rel="stylesheet">
<style>
:root{
  --teal:#0b6f66;
  --teal-dark:#075a53;
  --red:#7d0c0c;
  --ink:#222;
  --text:#444;
  --muted:#777;
  --grey-bg:#f1f1f1;
  --line:#d8d8d8;
  --badge:#d4dcdb;
  --white:#fff;
}
*{box-sizing:border-box;margin:0;padding:0}
html,body{width:1200px;height:3455px;overflow:hidden}
body{position:relative;background:var(--white);font-family:"Lato",sans-serif;color:var(--text);font-size:15px;line-height:1.45}
.abs{position:absolute}
.heading{font-family:"Oswald",sans-serif;font-weight:500;color:var(--ink);text-transform:uppercase}
.section-title{left:0;width:1200px;text-align:center;font-size:25px;letter-spacing:.5px}
.section-title::after{content:"";display:block;margin:8px auto 0;width:90px;height:3px;background:linear-gradient(90deg,#999 0 35%,transparent 35% 65%,#999 65%)}
.btn{display:inline-block;font-size:13px;text-align:center;color:var(--white);background:var(--teal);padding:9px 18px}
.btn-outline{background:var(--white);color:var(--muted);border:1px solid var(--line)}

/* header */
.site-header{left:0;top:0;width:1200px;height:92px;background:var(--white)}
.brand{left:104px;top:0;width:218px;height:112px;background:var(--white);border-radius:0 0 10px 10px;box-shadow:0 3px 8px rgba(0,0,0,.12);text-align:center;padding-top:30px;z-index:3}
.brand-dot{display:block;width:40px;height:40px;border-radius:50%;background:var(--teal);margin:0 auto 6px}
.brand-name{font-size:13px;font-weight:700;color:var(--teal)}
.top-contacts{right:72px;top:10px;font-size:13px;color:var(--ink);display:flex;align-items:center;gap:28px}
.top-contacts span{display:flex;align-items:center;gap:6px}
.header-book{background:var(--red);color:var(--white);font-size:12px;font-weight:700;padding:4px 14px;text-transform:uppercase;letter-spacing:.5px}
.main-nav{right:72px;top:52px;display:flex;gap:26px;font-size:16px;color:#333}
.main-nav .active{color:var(--teal);font-weight:700;border-bottom:2px solid var(--teal);padding-bottom:4px}

/* hero */
.hero{left:0;top:92px;width:1200px;height:468px;background:linear-gradient(180deg,#c9dfe6 0%,#a6c4cf 45%,#3f6e80 62%,#6d7f86 78%,#3a3a3a 100%)}
.hero-figure{left:700px;top:20px;width:320px;height:448px;background:linear-gradient(160deg,#6a4e45,#2a2a2a);opacity:.4;border-radius:45% 45% 0 0}
.hero-title{left:118px;top:190px;font-family:"Oswald",sans-serif;font-weight:400;font-size:42px;line-height:1.45;color:var(--teal);text-transform:uppercase}
.hero-outline{left:113px;top:336px;width:281px;height:45px;border:2px solid var(--teal);color:var(--teal);font-family:"Oswald",sans-serif;font-size:18px;display:flex;align-items:center;justify-content:center}
.book-now{left:111px;top:438px;width:281px;height:45px;background:var(--red);color:var(--white);font-family:"Oswald",sans-serif;font-size:18px;display:flex;align-items:center;justify-content:center}

/* practice */
.practice-card{top:675px;width:240px;height:315px;background:var(--white);box-shadow:0 2px 10px rgba(0,0,0,.18);text-align:center;padding:28px 20px 0}
.practice-icon{display:block;width:64px;height:74px;margin:0 auto 44px}
.practice-card h3{font-size:15px;font-weight:400;color:var(--ink);text-transform:uppercase;margin-bottom:4px}
.practice-card p{font-size:12.5px;color:var(--muted);line-height:1.35;height:66px;overflow:hidden;margin-bottom:16px}
.practice-card .btn{padding:6px 16px;font-size:12px}

/* relief */
.relief-bg{left:0;top:1025px;width:1200px;height:640px}
.relief-text{left:92px;width:770px}
.relief-text h2{font-family:"Oswald",sans-serif;font-weight:500;font-size:25px;line-height:1.1;color:var(--ink);text-transform:uppercase}
.relief-text h2::after{content:"";display:block;margin:8px 0 8px 50px;width:70px;height:3px;background:linear-gradient(90deg,#999 0 35%,transparent 35% 65%,#999 65%)}
.relief-text p{font-size:16px;color:var(--ink);line-height:1.55}

/* team */
.team-card{top:1718px;width:240px;height:187px;background:var(--teal);color:var(--white);overflow:hidden}
.team-card .who{position:absolute;left:24px;top:26px;font-size:13px;line-height:1.35;z-index:2}
.team-card .who b{display:block}
.team-photo{position:absolute;right:6px;top:10px;width:92px;height:177px;border-radius:46px 46px 0 0;background:linear-gradient(180deg,#d9c3a6,#f3f3f3)}
.team-bar{left:444px;top:1939px;width:332px;height:11px;background:var(--teal)}

/* free book */
.book-band{left:0;top:1950px;width:1200px;height:457px;background:var(--grey-bg)}
.book-cover{left:891px;top:2020px;width:230px;height:341px;background:linear-gradient(180deg,var(--teal) 0 42%,#7a9aa8 42%,#2e4d66 100%);box-shadow:8px 8px 14px rgba(0,0,0,.25)}
.book-cover span{position:absolute;left:14px;top:22px;color:var(--white);font-size:20px;font-weight:700}

/* cases */
.case-card{top:2510px;height:396px;background:var(--white);box-shadow:0 2px 10px rgba(0,0,0,.15)}
.case-card .photo{width:100%;height:219px}
.case-card h3{font-size:17px;font-weight:400;color:var(--ink);margin:14px 16px 4px;text-transform:uppercase}
.case-card p{font-size:13.5px;color:var(--text);margin:0 16px 12px;height:66px;overflow:hidden;line-height:1.6}
.case-card .btn{margin-left:16px}

/* contact */
.contact-block h3{font-size:20px;font-weight:400;color:var(--ink);text-transform:uppercase}
.contact-block p.intro{font-size:12.5px;color:var(--muted);width:380px;margin-top:12px}
.label{font-size:13px;font-weight:700;color:var(--ink);text-transform:uppercase}
.value{font-size:13px;color:var(--muted)}
.social{top:3290px;left:92px;display:flex;gap:9px}
.social span{width:30px;height:30px;border-radius:50%;background:var(--teal-dark);display:block}
.quote-box{left:624px;top:2956px;width:502px;height:372px;border:3px solid var(--teal);padding:44px 30px}
.field{position:absolute;border:1px solid var(--line);font-size:12px;color:#999;padding:7px 9px;background:var(--white)}
.send{position:absolute;left:324px;top:291px;width:143px;height:32px;background:var(--teal);color:var(--white);font-size:14px;display:flex;align-items:center;justify-content:center;text-transform:uppercase}

/* affiliates */
.affiliates{left:92px;top:3338px;width:1034px;height:30px;display:flex;justify-content:space-between;align-items:center}
.affiliate-badge{width:150px;height:26px;border-radius:13px;background:var(--badge)}

/* footer */
.site-footer{left:0;top:3376px;width:1200px;height:79px;background:var(--teal);color:var(--white);text-align:center;font-size:13px;padding-top:16px}
.site-footer nav{display:flex;justify-content:center;gap:14px}
.site-footer p{margin-top:5px}
</style>
</head>
<body>

<header class="site-header abs">
  <div class="brand abs"><span class="brand-dot"></span><span class="brand-name">Calderwyn Foot &amp; Ankle Clinic</span></div>
  <div class="top-contacts abs">
    <span><svg width="16" height="12" viewBox="0 0 16 12"><rect x="0.5" y="0.5" width="15" height="11" fill="var(--teal)"/><path d="M1 1l7 6 7-6" stroke="#fff" fill="none"/></svg>info@calderwynhealth.com.au</span>
    <span><svg width="14" height="14" viewBox="0 0 24 24"><path fill="var(--teal)" d="M6.6 10.8a15 15 0 0 0 6.6 6.6l2.2-2.2a1 1 0 0 1 1-.25 11 11 0 0 0 3.6.6 1 1 0 0 1 1 1V20a1 1 0 0 1-1 1A17 17 0 0 1 3 4a1 1 0 0 1 1-1h3.5a1 1 0 0 1 1 1 11 11 0 0 0 .6 3.6 1 1 0 0 1-.25 1z"/></svg>(08) 9450 2718</span>
    <span class="header-book">Book Now</span>
  </div>
  <nav class="main-nav abs">
    <span class="active">Home</span><span>Common Problems</span><span>Services</span><span>About</span><span>Case Histories</span><span>Blog</span><span>Helpful Infromation</span><span>Contact</span>
  </nav>
</header>

<section class="hero abs" role="img" aria-label="Athlete kneeling on a beach holding a sore ankle, sea in the background">
  <div class="hero-figure abs"></div>
</section>
<h1 class="hero-title abs">We offer solutions to<br>common foot problems</h1>
<div class="hero-outline abs">END YOUR SUFFERING TODAY</div>
<div class="book-now abs">BOOK NOW</div>

<h2 class="heading section-title abs" style="top:603px">Practice Areas</h2>

<div class="practice-card abs" style="left:92px">
  <span class="practice-icon" role="img" aria-label="Footprints icon" style="background:var(--teal);border-radius:30px 30px 20px 20px"></span>
  <h3>Common Problems</h3>
  <p style="color:var(--ink)">When you suffer from a foot and/or ankle problem, the pain and discomfort can make it a challenge to engage in simple</p>
  <span class="btn">Read More</span>
</div>
<div class="practice-card abs" style="left:357px">
  <span class="practice-icon" role="img" aria-label="Foot icon" style="background:#333;border-radius:8px 8px 30px 8px"></span>
  <h3>Foot &amp; Ankle Surgery</h3>
  <p>Foot and ankle pain can be extremely distracting and uncomfortable, and some conditions may require surgery.</p>
  <span class="btn btn-outline">Read More</span>
</div>
<div class="practice-card abs" style="left:622px">
  <span class="practice-icon" role="img" aria-label="Dancer icon" style="background:#333;border-radius:50%;width:50px"></span>
  <h3>Sport and Dance</h3>
  <p>Special patient groups require intensive and constant care to keep their feet and bodies healthy. We advise many</p>
  <span class="btn btn-outline">Read More</span>
</div>
<div class="practice-card abs" style="left:889px">
  <span class="practice-icon" role="img" aria-label="Foot silhouette icon" style="background:#333;border-radius:20px 20px 34px 10px;width:44px"></span>
  <h3>All Services</h3>
  <p>Foot, toe, or ankle pain can be severe and it can interfere with your ability to walk, stand, work, or do the activities that you</p>
  <span class="btn btn-outline">Read More</span>
</div>

<svg class="relief-bg abs" viewBox="0 0 1200 640" role="img" aria-label="Runner tying a shoe on a sunlit path">
  <defs>
    <linearGradient id="reliefFill" x1="0" y1="0" x2="1" y2="0">
      <stop offset="0" stop-color="#f4ede4"/>
      <stop offset=".6" stop-color="#ebdfcf"/>
      <stop offset=".78" stop-color="#d7b79a"/>
      <stop offset="1" stop-color="#c8a283"/>
    </linearGradient>
  </defs>
  <polygon points="0,57 1200,0 1200,472 0,640" fill="url(#reliefFill)"/>
</svg>
<div class="relief-text abs" style="top:1143px">
  <h2>Let our Westbrook podiatrists relieve<br>your foot and ankle pain</h2>
  <p>Whether you are an office worker, pensioner, or professional athlete, nearly all people will experience problems in their feet and ankles at some point in their lives. Unfortunately, a problem in the foot can affect the whole body, causing an infection to spread, deformities in the foot, and pain to travel upward into the leg.</p>
  <h2 style="margin-top:14px">A proven track record of correcting<br>foot pain in Perth patients</h2>
  <p>At the Calderwyn Foot &amp; Ankle Clinic, we know that there are often a variety of causes of foot and ankle pain, and each must be addressed to solve your problem for good. We examine your feet, posture, and gait to identify any biomechanical issues that could be causing your pain, treat ulcerations and foot eformities that prohibit full range of motion, and perform many different surgical techniques to ..</p>
</div>
<span class="btn abs" style="left:92px;top:1525px">Read More</span>

<h2 class="heading section-title abs" style="top:1652px">Our Team</h2>
<div class="team-card abs" style="left:92px"><div class="who"><b>Elise Varden</b>Podiatric Surgeon</div><div class="team-photo" role="img" aria-label="Portrait of Elise Varden"></div></div>
<div class="team-card abs" style="left:357px"><div class="who"><b>Marcus Holt</b>Podiatrist</div><div class="team-photo" role="img" aria-label="Portrait of Marcus Holt"></div></div>
<div class="team-card abs" style="left:622px"><div class="who"><b>Elise Varden</b>Podiatrist</div><div class="team-photo" role="img" aria-label="Portrait of Elise Varden"></div></div>
<div class="team-card abs" style="left:889px"><div class="who"><b>Nadia Kerrow</b>Podiatrist</div><div class="team-photo" role="img" aria-label="Portrait of Nadia Kerrow"></div></div>
<div class="team-bar abs"></div>

<section class="book-band abs"></section>
<h2 class="heading section-title abs" style="top:1988px">Free Book</h2>
<h3 class="abs" style="left:92px;top:2062px;font-size:20px;font-weight:400;color:var(--ink)">Free Foot Surgery Book by Podiatric Surgeon, Dr Owen Brack</h3>
<p class="abs" style="left:92px;top:2102px;width:700px;font-size:15px">This book was created to demonstrate examples of some foot conditions that can be &nbsp;surgically corrected by our Podiatric Surgeon, Dr Owen Brack.</p>
<span class="btn abs" style="left:92px;top:2170px">Read More</span>
<div class="book-cover abs" role="img" aria-label="Cover of the podiatric surgery book showing surgeons in theatre"><span>Podiatric Surgery</span></div>

<h2 class="heading section-title abs" style="top:2446px">Case Histories</h2>
<article class="case-card abs" style="left:92px;width:325px;box-shadow:0 6px 16px rgba(0,0,0,.3)">
  <div class="photo" role="img" aria-label="Hands massaging the sole of a foot" style="background:linear-gradient(135deg,#f4f4f4,#e6c9b4)"></div>
  <h3>Plantar Fascia Case</h3>
  <p>The case histories and outcomes presented here are for general information only and do not replace the advice of a health professional.</p>
  <span class="btn">Read More</span>
</article>
<article class="case-card abs" style="left:461px;width:299px">
  <div class="photo" role="img" aria-label="Feet with bunions on a wooden floor" style="background:linear-gradient(135deg,#7a3a24,#d79b83)"></div>
  <h3>Bunion Case</h3>
  <p>The case histories and outcomes presented here are for general information only and do not replace the advice of a</p>
  <span class="btn">Read More</span>
</article>
<article class="case-card abs" style="left:799px;width:327px">
  <div class="photo" role="img" aria-label="Doctor consulting with an older patient" style="background:linear-gradient(135deg,#e9eef2,#bfc9d2)"></div>
  <h3>Trauma Case</h3>
  <p>The case histories and outcomes presented here are for general information only and do not replace the advice of a health professional.</p>
  <span class="btn">Read More</span>
</article>

<div class="contact-block abs" style="left:92px;top:2994px">
  <h3>Get in Touch</h3>
  <p class="intro">Would you like to speak to one of our medical enquiry over the phone?Just submit your details and we'll be in tohch shortly</p>
  <div class="label" style="margin-top:22px">Address</div>
  <div class="value">Westbrook Office 22 Marlow Street Westbrook, WA 6150</div>
  <div class="label" style="margin-top:12px">Phone Number</div>
  <div class="value">Phone: (08) 9450 2718</div>
  <div class="label" style="margin-top:12px">Email</div>
  <div class="value">info@calderwynhealth.com.au</div>
  <div class="label" style="margin-top:12px">Follow Me</div>
</div>
<div class="social abs" role="img" aria-label="Social media links"><span></span><span></span><span></span><span></span><span></span><span></span></div>

<div class="quote-box abs contact-block">
  <h3 style="position:absolute;left:27px;top:36px">Request a Quick Quote</h3>
  <p class="intro" style="position:absolute;left:27px;top:78px;margin:0">Would you like to speak to one of our medical enquiry over the phone? Just submit your details and we'll be in tohch shortly</p>
  <div class="field" style="left:27px;top:143px;width:207px;height:33px">Your Name</div>
  <div class="field" style="left:257px;top:143px;width:210px;height:33px">Your Phone</div>
  <div class="field" style="left:27px;top:187px;width:207px;height:33px">Your Email</div>
  <div class="field" style="left:257px;top:187px;width:210px;height:84px">Your Message</div>
  <div class="field" style="left:27px;top:237px;width:207px;height:33px">I like to discuss</div>
  <div class="send">Send Request</div>
</div>

<div class="affiliates abs" role="img" aria-label="Trusted affiliate organisations">
  <span class="affiliate-badge"></span><span class="affiliate-badge"></span><span class="affiliate-badge"></span><span class="affiliate-badge"></span><span class="affiliate-badge"></span><span class="affiliate-badge"></span>
</div>

<footer class="site-footer abs">
  <nav><span>Home</span><span>/</span><span>About us</span><span>/</span><span>Medical Services</span><span>/</span><span>Our Team</span><span>/</span><span>Blog</span><span>/</span><span>Contact Us</span></nav>
  <p>© 2017 &nbsp;Calderwyn Foot &amp; Ankle Clinic. All Rights Reserved.</p>
</footer>

</body>
</html>
```